design a company brochure

tri-fold brochure. reference website: orvanta.llc for information (website under construction but should have the basic information)

Target Market(s)

Users of sign Language interpreting services; businesses, community, hospitals, schools, colleges, medical, religious, and legal settings

Industry/Entity Type

Community Service

Font styles to use
Serif
Decorative

Colors
734ea0
9ccb3b

Requirements
Must have
• Brochure should be worded so it applies to the above markets and focuses on our professionalism, integrity in business
Nice to have
• I would like the designers to look at the business website under construction (orvanta.llc) or an older website (orvanta-tkpr.com). Company was restructured and is now just ORVANTA, LLC.
A darker green than what is shown here. Again, reference the website
Should not have
• No personal pictures in the brochure - can use clip art or interpreter/interpreting shots.

```html
<!DOCTYPE html>
<html lang="en">
<head>
<meta charset="utf-8">
<title>ORVANTA, LLC — Tri-fold Brochure</title>
<link href="https://fonts.googleapis.com/css2?family=DM+Serif+Display&family=Montserrat:wght@400;500;600;700&display=swap" rel="stylesheet">
<style>
  :root{
    --purple:#6b3f9a;
    --purple-deep:#55307f;
    --purple-light:#7d52ad;
    --green:#8cc63f;
    --green-dark:#6fa52a;
    --ink:#3a3a3a;
    --paper:#ffffff;
    --page-bg:#eeeeee;
    --serif:'DM Serif Display', Georgia, serif;
    --sans:'Montserrat', Arial, sans-serif;
  }
  *{box-sizing:border-box;margin:0;padding:0}
  html,body{width:1200px;height:4000px;overflow:hidden}
  body{background:var(--page-bg);font-family:var(--sans);color:var(--ink);position:relative}

  .spread{position:absolute;left:100px;width:1000px;height:720px;display:flex;background:var(--paper);box-shadow:0 6px 24px rgba(0,0,0,.18)}
  .spread--outside{top:1180px}
  .spread--inside{top:2100px;border-bottom:7px solid var(--green)}
  .panel{width:333.33px;height:100%;position:relative;overflow:hidden}
  .panel--white{background:var(--paper);padding:34px 28px 20px}
  .panel--purple{background:linear-gradient(180deg,var(--purple-light) 0%,var(--purple) 45%,var(--purple-deep) 100%);color:#fff}

  .heading{font-family:var(--serif);color:var(--purple);font-size:29px;letter-spacing:.5px;text-transform:uppercase;line-height:1}
  .body-text{font-size:7.6px;line-height:1.5;color:#444}
  .photo{display:block}

  /* About */
  .bio{display:flex;gap:10px;margin-top:20px}
  .bio__figure{width:96px;flex:none}
  .bio__photo{width:96px;height:120px}
  .bio__tag{background:var(--green);color:var(--purple-deep);font-size:8px;font-weight:700;padding:4px 6px;line-height:1.15}
  .bio__tag span{display:block;font-weight:500}
  .bio__text{flex:1}
  .about__tail{margin-top:4px}

  /* Brand mark */
  .brand{display:flex;align-items:center;gap:8px}
  .brand__square{width:16px;height:16px;flex:none}
  .brand__name{font-family:var(--serif);font-size:20px;letter-spacing:.5px}

  /* Contact */
  .contact{padding:34px 26px 0;text-align:center}
  .contact .brand{justify-content:center;color:#fff}
  .contact .brand__square{background:var(--green)}
  .contact__title{font-family:var(--serif);font-size:32px;margin:64px 0 20px;letter-spacing:.5px}
  .contact__intro{font-size:7.6px;line-height:1.5;color:#eee}
  .contact__list{list-style:none;margin-top:30px}
  .contact__item{display:flex;flex-direction:column;align-items:center;gap:6px;margin-bottom:14px;font-size:12px}
  .contact__item svg{width:15px;height:15px}
  .contact__foot{font-size:8px;line-height:1.45;margin-top:20px;color:#eee}

  /* Cover */
  .cover__top{height:175px;position:relative;padding:40px 0 0 40px}
  .cover__strip{position:absolute;right:0;top:0;width:34px;height:175px;background:var(--green)}
  .cover .brand{color:var(--purple)}
  .cover .brand__square{background:var(--purple)}
  .cover__photo{width:100%;height:295px}
  .cover__bottom{position:relative;padding:24px 26px 0 66px;height:250px}
  .cover__bar{position:absolute;left:0;top:0;width:34px;height:100%;background:var(--green)}
  .cover__title{font-family:var(--serif);color:var(--purple);font-size:31px;line-height:1}
  .cover__text{font-size:12px;line-height:1.55;color:#333;margin-top:12px}
  .cover__url{font-family:var(--serif);font-size:17px;margin-top:14px;color:#222}

  /* Services */
  .services__intro{margin-top:14px}
  .services__lead{font-size:7.6px;font-weight:700;line-height:1.45;margin-top:10px;color:#333}
  .service{margin-top:20px}
  .service__photo{width:100%;height:96px}
  .service__label{background:var(--green);color:var(--purple-deep);font-weight:700;font-size:12px;letter-spacing:1px;text-transform:uppercase;padding:5px 12px;margin:-18px 0 0 0;position:relative;width:100%}
  .bullets{display:grid;grid-template-columns:1fr 1fr;gap:4px 10px;list-style:none;margin-top:9px;font-size:7.4px;font-weight:600;color:#333;padding-left:4px}
  .bullets li{position:relative;padding-left:9px;line-height:1.3}
  .bullets li::before{content:"";position:absolute;left:0;top:2px;width:5px;height:5px;border-radius:50%;background:var(--purple)}

  /* Purple services column */
  .occasions{padding:34px 28px 0}
  .occasion{margin-bottom:16px}
  .occasion__photo{width:100%;height:104px}
  .occasion__label{background:var(--green);color:var(--purple-deep);font-weight:700;font-size:12px;letter-spacing:1px;text-transform:uppercase;padding:5px 12px}
  .occasion .bullets{color:#fff}
  .occasion .bullets li::before{background:#fff}
  .occasions__foot{font-size:7.6px;line-height:1.45;text-align:center;color:#eee;margin-top:6px}

  /* Resources */
  .qa{display:flex;gap:6px;margin-top:12px}
  .qa__marks{font-family:var(--serif);font-size:11px;line-height:1.05;color:var(--green-dark);flex:none;width:10px}
  .qa__marks b{display:block;font-weight:400;color:var(--purple)}
  .qa__q{font-size:6.8px;font-weight:700;color:var(--green-dark);text-transform:uppercase;line-height:1.3}
  .qa__a{font-size:6.8px;line-height:1.45;color:#444;margin-top:2px}
  .faq-heading{margin-top:22px;font-size:24px}
</style>
</head>
<body>

<section class="spread spread--outside">

  <div class="panel panel--white about">
    <h2 class="heading">About us</h2>

    <div class="bio">
      <div class="bio__figure">
        <div class="photo bio__photo" role="img" aria-label="Portrait photo of the owner" style="background:linear-gradient(160deg,#8a8f86,#4e4f4a)"></div>
        <p class="bio__tag">Dana Whitfield<span>Owner</span></p>
      </div>
      <p class="body-text bio__text">Dana Whitfield is a native of Iowa but has lived in Colorado long enough to call it home. She graduated in 1998 from Ridgeline Community College with an A.A.S. degree in Interpreter Preparation and has done most of her interpreting work in the educational interpreting field. She is currently enrolled in the ASL-English Interpretation BA program at the University of the High Plains.</p>
    </div>

    <div class="bio">
      <div class="bio__figure">
        <div class="photo bio__photo" role="img" aria-label="Portrait photo of the staffing coordinator" style="background:linear-gradient(160deg,#9a8a7c,#4a3f3a)"></div>
        <p class="bio__tag">Lena Marsh<span>Staffing Coordinator</span></p>
      </div>
      <p class="body-text bio__text">Recognizing the great need for qualified interpreters in the public education system, she partnered with Lena Marsh to offer school districts state Department of Education credentialed interpreters for Deaf and Hard of Hearing students. By using credentialed interpreters, school districts are able to maintain compliance with state rules, as well as securing professional</p>
    </div>

    <p class="body-text about__tail">and highly qualified interpreters for their students. Lena Marsh is the staffing coordinator of ORVANTA, LLC. She grew up in California and moved to Colorado in 1996. She graduated from Ridgeline Community College in 2002 earning her A.A.S in Interpreter Preparation. She is currently obtaining her B.S in Speech Language and Hearing Sciences. In her spare time, she enjoys spending time with her family and friends and volunteering at her church.</p>
  </div>

  <div class="panel panel--purple contact">
    <div class="brand"><span class="brand__square"></span><span class="brand__name">ORVANTA, LLC</span></div>
    <h2 class="contact__title">CONTACT US</h2>
    <p class="contact__intro">Thank you for your interest in ORVANTA / TKPR. If you have any questions about our services or would like to schedule an interpreter, please contact us using the information below or fill out the Request an Interpreter form and one of our staff will contact you promptly. We are available 24 hours a day 7 days a week to assist you with your interpreting needs.</p>
    <ul class="contact__list">
      <li class="contact__item">
        <svg viewBox="0 0 24 24" fill="none" stroke="#fff" stroke-width="2"><circle cx="12" cy="12" r="10"/><path d="M2 12h20M12 2c3 3 3 17 0 20M12 2c-3 3-3 17 0 20"/></svg>
        ORVANTA / TKPR, LLC
      </li>
      <li class="contact__item">
        <svg viewBox="0 0 24 24" fill="none" stroke="#fff" stroke-width="2"><rect x="2" y="5" width="20" height="14" rx="1"/><path d="M2 6l10 7 10-7"/></svg>
        (720) 555-0148
      </li>
      <li class="contact__item">
        <svg viewBox="0 0 24 24" fill="#fff"><path d="M6.6 10.8a15 15 0 0 0 6.6 6.6l2.2-2.2a1 1 0 0 1 1-.25 11.4 11.4 0 0 0 3.6.6 1 1 0 0 1 1 1V20a1 1 0 0 1-1 1A17 17 0 0 1 3 4a1 1 0 0 1 1-1h3.5a1 1 0 0 1 1 1c0 1.25.2 2.450.57 3.57a1 1 0 0 1-.25 1z"/></svg>
        (303) 555-0172
      </li>
      <li class="contact__item">
        <svg viewBox="0 0 24 24" fill="#fff"><path d="M12 2a7 7 0 0 0-7 7c0 5.2 7 13 7 13s7-7.8 7-13a7 7 0 0 0-7-7zm0 9.5A2.5 2.5 0 1 1 12 6.5a2.5 2.5 0 0 1 0 5z"/></svg>
        PO BOX 40512<br>Denver, Colorado 80299
      </li>
    </ul>
    <p class="contact__foot">ORVANTA / TKPR, LLC &nbsp;|&nbsp; VOICE : (720) 555-0148<br>| TEXT : (303) 555-0172 &nbsp;|&nbsp; PO BOX 40512 |<br>DENVER, CO 80299</p>
  </div>

  <div class="panel cover">
    <div class="cover__top">
      <div class="brand"><span class="brand__square"></span><span class="brand__name">ORVANTA, LLC</span></div>
      <div class="cover__strip"></div>
    </div>
    <div class="photo cover__photo" role="img" aria-label="Photo of two hands signing in front of pine needles" style="background:radial-gradient(ellipse at 55% 55%,#c9a890 0%,#5e7a3a 35%,#2f4a1f 75%,#1e3214 100%)"></div>
    <div class="cover__bottom">
      <div class="cover__bar"></div>
      <h1 class="cover__title">Let’s connect!</h1>
      <p class="cover__text">we connect with the best interpreter for your needs and situaion, give you confidence &nbsp;that our staff will be there for you</p>
      <p class="cover__url">orvanta.llc</p>
    </div>
  </div>
</section>

<section class="spread spread--inside">

  <div class="panel panel--white services">
    <h2 class="heading">Our services</h2>
    <p class="body-text services__intro">Orvanta Interpreting Group is the Denver Metro area's premier interpreting agency. We have been providing qualified professional Sign Language Interpreting services since 2008. Our interpreters are carefully screened and handpicked to ensure that your communication needs are met with ease and comfort. We offer superior service at competitive prices with excellent customer service.</p>
    <p class="services__lead">Although we specialize in Medical and Educational interpreting, we also provide services for:</p>

    <div class="service">
      <div class="photo service__photo" role="img" aria-label="Photo of students studying together at a table" style="background:linear-gradient(135deg,#c7b7a6,#7b8a9a 60%,#4d5968)"></div>
      <p class="service__label">Educational</p>
      <ul class="bullets">
        <li>K-12 Settings</li><li>IEP Meetings</li>
        <li>Post-Secondary</li><li>Staff Meetings</li>
        <li>Parent/Teacher Conference</li><li>Extracurricular Activities</li>
      </ul>
    </div>

    <div class="service">
      <div class="photo service__photo" role="img" aria-label="Photo of a doctor speaking with a patient" style="background:linear-gradient(135deg,#dfe6ec,#9fb3c6 55%,#5f7489)"></div>
      <p class="service__label">Medical</p>
      <ul class="bullets">
        <li>Doctor's Appointments</li><li>Doctor's Appointments</li>
        <li>ER Visits</li><li>ER Visits</li>
        <li>Patient Education and Counseling</li><li>Patient Education and Counseling</li>
      </ul>
    </div>
  </div>

  <div class="panel panel--purple occasions">
    <div class="occasion">
      <div class="photo occasion__photo" role="img" aria-label="Photo of a business meeting with a laptop and paperwork" style="background:linear-gradient(135deg,#d9d4cc,#8f8a82 55%,#3c3a38)"></div>
      <p class="occasion__label">Business</p>
      <ul class="bullets">
        <li>Staff Meetings</li><li>Conferences</li>
        <li>Interviews &amp; Orientations</li><li>Job Training</li>
      </ul>
    </div>
    <div class="occasion">
      <div class="photo occasion__photo" role="img" aria-label="Photo of a wedding couple holding hands with flowers" style="background:linear-gradient(135deg,#eeeae4,#b9b2a8 55%,#6d665e)"></div>
      <p class="occasion__label">Special occasions</p>
      <ul class="bullets">
        <li>Weddings</li><li>Funerals</li>
        <li>Graduations</li>
      </ul>
    </div>
    <div class="occasion">
      <div class="photo occasion__photo" role="img" aria-label="Photo of a white church under a blue sky" style="background:linear-gradient(180deg,#5c8fcf 0%,#9fc0e4 50%,#e6e6e2 70%,#5d7a3f 100%)"></div>
      <p class="occasion__label">Religious</p>
      <ul class="bullets">
        <li>Church Services &amp; Sermons</li><li>Religious Ceremonies</li>
        <li>Counseling</li>
      </ul>
    </div>
    <p class="occasions__foot">ORVANTA / TKPR, LLC &nbsp;|&nbsp; VOICE : (720) 555-0148 |<br>TEXT : (303) 555-0172 &nbsp;|&nbsp; PO BOX 40512 |<br>DENVER, CO 80299</p>
  </div>

  <div class="panel panel--white resources">
    <h2 class="heading">Resources</h2>

    <div class="qa">
      <p class="qa__marks">Q.<b>A.</b></p>
      <div>
        <p class="qa__q">When do I need to request an interpreter?</p>
        <p class="qa__a">Sign language interpreters are needed when you communicate with a deaf individual whose primary source of communication is sign language. Always ask the deaf person first if an interpreter is needed. A deaf person who is competent in English when writing, reading and speaking may still want an interpreter for more complex or technical situations to ensure effective communication. Lip reading for some deaf people is tiring and is not a reliable means of understanding a conversation in its entirety.</p>
      </div>
    </div>

    <div class="qa">
      <p class="qa__marks">Q.<b>A.</b></p>
      <div>
        <p class="qa__q">Rights of deaf and hard of hearing/ADA</p>
        <p class="qa__a">The Americans with Disability Act (ADA) is a law that prohibits discrimination against people with disabilities including deaf and hard of hearing individuals. All businesses and government agencies are required to provide effective communication. Please visit www.access-rights.example for more information.</p>
      </div>
    </div>

    <div class="qa">
      <p class="qa__marks">Q.<b>A.</b></p>
      <div>
        <p class="qa__q">Benefits to small businesses</p>
        <p class="qa__a">Small businesses may qualify for a tax credit under Section 44 of the Internal Revenue Code. This tax incentive was created in 1990 to help small businesses cover ADA related expenses. For more information please visit www.tax-help.example.</p>
      </div>
    </div>

    <h2 class="heading faq-heading">FAQ’s</h2>

    <div class="qa">
      <p class="qa__marks">Q.<b>A.</b></p>
      <div>
        <p class="qa__q">Can the deaf person bring in their own interpreter?</p>
        <p class="qa__a">It is not recommended. Professional interpreters are trained and must abide by the professional Code of Conduct. This will ensure message accuracy, impartiality and confidentiality.</p>
      </div>
    </div>

    <div class="qa">
      <p class="qa__marks">Q.<b>A.</b></p>
      <div>
        <p class="qa__q">Is there always a two hour minimum?</p>
        <p class="qa__a">Many assignments require a two hour minimum however we are more than happy to come up with an agreement that fits your needs.</p>
      </div>
    </div>

    <div class="qa">
      <p class="qa__marks">Q.<b>A.</b></p>
      <div>
        <p class="qa__q">Do you only supply educational interpreters?</p>
        <p class="qa__a">Although our main focus is educational interpreting, we do provide services for medical and community interpreting as well.</p>
      </div>
    </div>
  </div>
</section>

</body>
</html>
```